PitchTally Webpages and Logo

See attached brief. Take the existing website www.pitchtally.co.uk and logo and transform these assets to:

Give people who arrive on the site for first time the confidence to sign-up easily and quickly
Allow regular returning users quick and easy placing of predictions and encourage them to share the PitchTally prediction on social networks and with their contacts
Convey the essence of a community working together to enjoyably come-up with smart predictions on sporting events
Work seamlessly and well across smartphones, tablets and desktop i.e. Should be Responsive Web Design
Updates

Target Market(s)

Users are sports fans with opinions
Primarily male and early twenties to mid-thirties
They are competitive - they want to beat their peers
Many are from outside the UK

Industry/Entity Type

Events

Logo Text

PitchTally

Coding

Coded - Design and coding required

Number of Pages Required

4 page

Font styles to use
Sans Serif

Requirements
Must have
• Responsive Web Design
• Mobile First
• HTML must work with dedicated bespoke application developed in ASP.NET using MS SQL underneath
• See Brief
Nice to have
• See brief
Should not have
• See brief

```html
<!DOCTYPE html>
<html lang="en">
<head>
<meta charset="utf-8">
<title>PitchTally</title>
<link rel="stylesheet" href="https://fonts.googleapis.com/css2?family=Lato:wght@300;400;700;900&display=swap">
<style>
:root{
  --navy:#0d3b6e;
  --blue:#2f80c9;
  --orange:#ff5a36;
  --green:#00b05a;
  --teal:#19a98a;
  --yellow:#f5d313;
  --ink:#222;
  --muted:#555;
  --line:#e3e3e3;
  --panel:#f4f4f4;
  --band:#ececec;
  --dark:#121212;
  --footer:#222;
}
*{box-sizing:border-box;margin:0;padding:0}
html,body{width:1200px;height:2691px;overflow:hidden}
body{font-family:"Lato",sans-serif;color:var(--ink);background:#fff;position:relative}
.abs{position:absolute}

/* header */
.site-header{position:absolute;left:0;top:0;width:1200px;height:93px;background:#fff;box-shadow:0 2px 6px rgba(0,0,0,.12);z-index:2}
.brand{position:absolute;left:111px;top:22px;display:flex;align-items:center;gap:12px}
.brand-dot{width:52px;height:52px;border-radius:50%;background:var(--blue)}
.brand-name{font-weight:900;font-size:30px;color:var(--navy)}
.main-nav{position:absolute;right:111px;top:32px;display:flex;align-items:center;gap:0}
.main-nav a{font-size:16px;color:var(--ink);text-decoration:none;margin-left:34px;letter-spacing:.3px}
.main-nav a.active{color:var(--blue)}
.main-nav .signup{background:var(--navy);color:#fff;padding:8px 28px;border-radius:4px;font-weight:700;margin-left:40px}

/* hero */
.hero-band{position:absolute;left:0;top:93px;width:1200px;height:558px;background:var(--band)}
.hero{position:absolute;left:111px;top:120px;width:974px;height:504px;display:flex}
.hero-copy{width:395px;height:504px;background:linear-gradient(180deg,#1b1d19,#2b2f26);color:#fff;text-align:center;padding-top:48px}
.hero-copy h1{font-weight:400;font-size:26px;line-height:35px}
.hero-copy h1 strong{color:var(--yellow);font-weight:700}
.hero-copy .accent{color:var(--yellow)}
.hero-copy p{font-size:21px;line-height:31px;margin-top:4px}
.hero-copy .free{color:var(--yellow);font-weight:700;margin-top:10px}
.btn{display:block;width:247px;height:52px;margin:0 auto;border-radius:3px;color:#fff;font-weight:700;font-size:21px;line-height:52px;text-decoration:none}
.btn-join{background:var(--blue);margin-top:30px}
.btn-play{background:var(--orange);margin-top:18px}
.hero-photo{width:579px;height:504px;background:linear-gradient(180deg,#3b4a5e 0%,#5a6b7e 40%,#3c7a34 62%,#4f9a3e 100%);position:relative}
.slide-dots{position:absolute;right:18px;bottom:14px;display:flex;gap:5px}
.slide-dots span{width:9px;height:9px;border-radius:50%;background:#fff}
.slide-dots span.on{background:transparent;border:1.5px solid #fff}

/* stats */
.stats{position:absolute;left:0;top:651px;width:1200px;height:314px;background:radial-gradient(ellipse at center,#2a2a2a 0%,var(--dark) 75%)}
.stat{position:absolute;top:45px;width:320px;text-align:center;color:#fff}
.stat h3{font-weight:400;font-size:26px;letter-spacing:.5px}
.stat .pct{font-size:52px;font-weight:400;line-height:60px}
.stat .row{display:flex;justify-content:center;gap:80px;margin-top:22px}
.stat .crest{width:90px;height:90px;border-radius:50%;box-shadow:0 18px 14px -8px rgba(0,0,0,.9)}
.stat .cap{font-size:15px;margin-top:18px}
.stat .caps{display:flex;justify-content:center;gap:130px}

/* predictions */
.section-title{position:absolute;font-weight:300;font-size:32px;color:var(--ink);letter-spacing:.5px}
.card{position:absolute;width:309px;height:221px;background:#fafafa;border:1px solid var(--line)}
.card .date{text-align:center;font-size:15px;margin-top:20px;color:#333}
.card .match{display:flex;justify-content:space-between;align-items:center;padding:0 22px;margin-top:24px}
.card .team{width:110px;text-align:center;font-size:11.5px;color:#333}
.card .team i{display:block;width:62px;height:62px;border-radius:50%;margin:0 auto 10px}
.card .v{font-size:13px;margin-top:-20px}
.card .predict{position:absolute;left:-1px;bottom:-1px;width:309px;height:45px;background:var(--orange);color:#fff;font-size:12px;text-align:center;line-height:45px;letter-spacing:.3px}

/* tables */
.tabs{position:absolute;left:111px;top:1684px;display:flex;gap:5px}
.tabs span{width:178px;height:54px;background:#000;color:#fff;font-size:21px;text-align:center;line-height:54px;font-weight:300}
.tabs span.active{background:var(--green)}
.league{position:absolute;left:111px;top:1738px;width:978px;border-collapse:collapse;background:var(--panel)}
.league th{height:60px;font-weight:400;font-size:20px;text-align:left;border-right:1px solid #fff}
.league td{height:117.5px;border-top:1px solid #fff;border-right:1px solid #fff;vertical-align:middle;font-size:14px}
.league .c-rank{width:140px;text-align:center;font-size:20px}
.league th.c-rank{text-align:center}
.league .c-player{width:379px;padding-left:40px}
.league .c-team{width:206px;text-align:center}
.league th.c-team{text-align:center}
.league .c-total{padding-left:36px}
.player{display:flex;align-items:center;gap:14px}
.avatar{width:70px;height:70px;border-radius:50%;background:linear-gradient(135deg,#6d8aa3,#3d5670)}
.player b{display:block;font-weight:400;color:var(--teal);font-size:15px}
.player small{font-size:11px;color:#333}
.club{display:inline-block;width:66px;height:66px;border-radius:50%}
.view-more{position:absolute;left:111px;top:2504px;width:978px;height:62px;background:var(--green);color:#fff;text-align:center;line-height:62px;font-size:16px;letter-spacing:.4px}
.view-more svg{vertical-align:middle;margin-left:6px}

/* footer */
.site-footer{position:absolute;left:0;top:2583px;width:1200px;height:108px;background:var(--footer);color:#eee;text-align:center;font-size:13.5px}
.site-footer nav{margin-top:30px}
.site-footer nav a{color:#eee;text-decoration:none}
.site-footer nav span{margin:0 10px}
.site-footer p{margin-top:14px}
</style>
</head>
<body>

<header class="site-header">
  <div class="brand"><span class="brand-dot"></span><span class="brand-name">PitchTally</span></div>
  <nav class="main-nav">
    <a class="active" href="#">HOME</a>
    <a href="#">TABLES</a>
    <a href="#">KITTY</a>
    <a href="#">INFORMATION PAGES</a>
    <a class="signup" href="#">SIGN UP</a>
  </nav>
</header>

<div class="hero-band"></div>
<section class="hero">
  <div class="hero-copy">
    <h1>Predict results, scores and<br>scorers for your free chance<br>to win a <strong>£20 ShopNest</strong><br><span class="accent">Voucher</span> every week.</h1>
    <p>Overall season winner gets up to<br>£1000 in ShopNest vouchers!</p>
    <p class="free">No entry fee and no catches.</p>
    <a class="btn btn-join" href="#">JOIN NOW !</a>
    <a class="btn btn-play" href="#">PLAY NOW FOR FREE</a>
  </div>
  <div class="hero-photo" role="img" aria-label="Footballer in blue kit dribbling a ball on a stadium pitch">
    <div class="slide-dots"><span class="on"></span><span></span><span></span><span></span></div>
  </div>
</section>

<section class="stats">
  <div class="stat" style="left:109px">
    <h3>RESULT</h3><div class="pct" style="color:var(--yellow)">100%</div>
    <div class="row"><i class="crest" style="background:#d8262a"></i></div>
    <div class="cap">Winner</div>
  </div>
  <div class="stat" style="left:436px">
    <h3>SCORE</h3><div class="pct" style="color:var(--orange)">100%</div>
    <div class="row"><i class="crest" style="background:#d8262a"></i><i class="crest" style="background:#7a1f3d"></i></div>
    <div class="caps cap"><span>2</span><span>0</span></div>
  </div>
  <div class="stat" style="left:771px">
    <h3>1ST GOAL</h3><div class="pct" style="color:var(--teal)">80%</div>
    <div class="row"><i class="crest" role="img" aria-label="Player portrait" style="background:linear-gradient(135deg,#c9c9c9,#7a7a7a);border:3px solid #fff"></i></div>
    <div class="cap">Wes Rowan</div>
  </div>
</section>

<h2 class="section-title" style="left:0;width:1200px;text-align:center;top:1004px">OUR PREDICTIONS</h2>

<article class="card" style="left:111px;top:1078px"><div class="date">Sat 20 Dec 2014 12:45 PM</div><div class="match"><div class="team"><i style="background:#274b9f"></i>Eastford</div><span class="v">v</span><div class="team"><i style="background:#6cabdd"></i>Northgate City</div></div><div class="predict">PREDICT YOUR SCORE !</div></article>
<article class="card" style="left:445px;top:1078px"><div class="date">Sat 20 Dec 2014 12:45 PM</div><div class="match"><div class="team"><i style="background:#0a4595"></i>Eastford</div><span class="v">v</span><div class="team"><i style="background:#7a1f3d"></i>Northgate City</div></div><div class="predict">PREDICT YOUR SCORE !</div></article>
<article class="card" style="left:779px;top:1078px"><div class="date">Sat 20 Dec 2014 12:45 PM</div><div class="match"><div class="team"><i style="background:#118a45"></i>Eastford</div><span class="v">v</span><div class="team"><i style="background:#d71920"></i>Northgate City</div></div><div class="predict">PREDICT YOUR SCORE !</div></article>
<article class="card" style="left:111px;top:1337px"><div class="date">Sat 20 Dec 2014 12:45 PM</div><div class="match"><div class="team"><i style="background:#1a1a1a"></i>Eastford</div><span class="v">v</span><div class="team"><i style="background:#c8102e"></i>Northgate City</div></div><div class="predict">PREDICT YOUR SCORE !</div></article>
<article class="card" style="left:445px;top:1337px"><div class="date">Sat 20 Dec 2014 12:45 PM</div><div class="match"><div class="team"><i style="background:#7a263a"></i>Eastford</div><span class="v">v</span><div class="team"><i style="background:#95bfe5"></i>Northgate City</div></div><div class="predict">PREDICT YOUR SCORE !</div></article>
<article class="card" style="left:779px;top:1337px"><div class="date">Sat 20 Dec 2014 12:45 PM</div><div class="match"><div class="team"><i style="background:#3a3a3a"></i>Eastford</div><span class="v">v</span><div class="team"><i style="background:#a50044"></i>Northgate City</div></div><div class="predict">PREDICT YOUR SCORE !</div></article>

<h2 class="section-title" style="left:111px;top:1618px">TABLES</h2>
<div class="tabs"><span class="active">Season</span><span>Monthly</span><span>Weekly</span><span>Statistics</span><span>Mini-liga</span></div>

<table class="league">
  <thead><tr><th class="c-rank">Rank</th><th class="c-player">Players</th><th class="c-team">Team</th><th class="c-total">Total</th></tr></thead>
  <tbody>
    <tr><td class="c-rank">1</td><td class="c-player"><div class="player"><i class="avatar" role="img" aria-label="Player photo"></i><div><b>Theo Harland</b><small>Ashbury</small></div></div></td><td class="c-team"><i class="club" style="background:#0a4595"></i></td><td class="c-total">218 , Kitty prize &nbsp;| £515.60</td></tr>
    <tr><td class="c-rank">2</td><td class="c-player"><div class="player"><i class="avatar" role="img" aria-label="Player photo"></i><div><b>Theo Harland</b><small>Ashbury</small></div></div></td><td class="c-team"><i class="club" style="background:#3a3a3a"></i></td><td class="c-total">218 , Kitty prize &nbsp;| £515.60</td></tr>
    <tr><td class="c-rank">3</td><td class="c-player"><div class="player"><i class="avatar" role="img" aria-label="Player photo"></i><div><b>Theo Harland</b><small>Ashbury</small></div></div></td><td class="c-team"><i class="club" style="background:#a50044"></i></td><td class="c-total">218 , Kitty prize &nbsp;| £515.60</td></tr>
    <tr><td class="c-rank">4</td><td class="c-player"><div class="player"><i class="avatar" role="img" aria-label="Player photo"></i><div><b>Theo Harland</b><small>Ashbury</small></div></div></td><td class="c-team"><i class="club" style="background:#d71920"></i></td><td class="c-total">218 , Kitty prize &nbsp;| £515.60</td></tr>
    <tr><td class="c-rank">5</td><td class="c-player"><div class="player"><i class="avatar" role="img" aria-label="Player photo"></i><div><b>Theo Harland</b><small>Ashbury</small></div></div></td><td class="c-team"><i class="club" style="background:#132257"></i></td><td class="c-total">218 , Kitty prize &nbsp;| £515.60</td></tr>
    <tr><td class="c-rank">6</td><td class="c-player"><div class="player"><i class="avatar" role="img" aria-label="Player photo"></i><div><b>Theo Harland</b><small>Ashbury</small></div></div></td><td class="c-team"><i class="club" style="background:#118a45"></i></td><td class="c-total">218 , Kitty prize &nbsp;| £515.60</td></tr>
  </tbody>
</table>

<a class="view-more">CLICK HERE TO VIEW MORE <svg width="16" height="16" viewBox="0 0 16 16"><circle cx="8" cy="8" r="8" fill="#fff"/><path d="M6.5 4.5 10 8l-3.5 3.5" stroke="#00b05a" stroke-width="2" fill="none"/></svg></a>

<footer class="site-footer">
  <nav><a href="#">FAQ</a><span>|</span><a href="#">Profile</a><span>|</span><a href="#">History</a><span>|</span><a href="#">Mini-Liga Admin</a><span>|</span><a href="#">About</a><span>|</span><a href="#">Contact</a><span>|</span><a href="#">Privacy</a><span>|</span><a href="#">Terms</a></nav>
  <p>© 2014 Company Name | All Rights Reserved</p>
</footer>

</body>
</html>
```